Flier redesign

Sample fliers are attached from previous 2 years "Seasonal care 2018" and "2019 Seasonal Care" . Need an updated design for this year.

Possible images are attached to this brief. If you use the before/after pictures - you should use both of them. Use images attached to this brief or any from our website that you may prefer.

Colors

Designer to choose colors to be used in the design.

Requirements
Must have
• Colors should match our website theme. www.hollowbrookgardens.org
• Should be a "new" design, not just copying one of the prior year designs with a different image.
• Must be created in photoshop and file must be provided at the end.
• Text should be the same as 2019 version.

```html
<!DOCTYPE html>
<html lang="en">
<head>
<meta charset="utf-8">
<title>Hollowbrook Gardens – 2019 Landscaping Packages</title>
<link href="https://fonts.googleapis.com/css2?family=Open+Sans:ital,wght@0,400;0,600;0,700;0,800;1,400;1,600;1,700&display=swap" rel="stylesheet">
<style>
  :root {
    --maroon: #7a2131;
    --orange: #f26b3a;
    --charcoal: #4b4b4d;
    --mist: #e6e6e6;
    --paper: #ffffff;
    --ink: #222222;
    --stage: #d2d2d2;
  }
  * { box-sizing: border-box; margin: 0; padding: 0; }
  html, body { width: 1039px; height: 1200px; overflow: hidden; }
  body {
    background: var(--stage);
    font-family: "Open Sans", Arial, sans-serif;
    color: var(--ink);
    position: relative;
  }
  .flier {
    position: absolute;
    left: 69px; top: 18px;
    width: 900px; height: 1164px;
    background: var(--mist);
    overflow: hidden;
  }
  .masthead {
    position: absolute; left: 0; top: 0;
    width: 100%; height: 156px;
    background: var(--paper);
    display: flex; align-items: center; justify-content: center; gap: 16px;
  }
  .masthead__dot {
    width: 22px; height: 22px; border-radius: 50%;
    background: var(--maroon);
  }
  .masthead__name {
    font-weight: 600; font-size: 40px; letter-spacing: 2px;
    text-transform: uppercase; color: var(--maroon);
  }
  .hero-photo {
    position: absolute; left: 0; top: 156px;
    width: 100%; height: 518px;
    background:
      linear-gradient(180deg, #9ea3a6 0%, #8c9289 22%, #6f8a55 45%, #5e8a3a 65%, #4f7a30 100%);
  }
  .footer-band {
    position: absolute; left: 0; bottom: 0;
    width: 100%; height: 72px;
    background: var(--maroon);
  }
  .year-badge {
    position: absolute; left: 0; top: 243px;
    width: 226px; height: 124px;
    background: var(--maroon);
    border-radius: 0 38px 38px 0;
    color: var(--paper);
    padding: 10px 0 0 30px;
  }
  .year-badge__year { font-weight: 800; font-size: 66px; line-height: 62px; letter-spacing: 1px; }
  .year-badge__title { font-weight: 700; font-size: 22px; line-height: 26px; }

  .package {
    position: absolute;
    width: 250px;
    bottom: 54px;
    display: flex; flex-direction: column;
  }
  .package--seasonal { left: 54px; top: 608px; }
  .package--basic { left: 326px; top: 552px; }
  .package--perpetual { left: 597px; top: 444px; }

  .package__flag {
    background: var(--orange); color: var(--paper);
    height: 38px; border-radius: 14px 14px 0 0;
    font-weight: 700; font-size: 23px; text-align: center; line-height: 38px;
  }
  .package__title {
    background: var(--maroon); color: var(--paper);
    font-weight: 700; text-align: center; text-transform: uppercase;
    display: flex; align-items: center; justify-content: center;
  }
  .package--seasonal .package__title { height: 66px; font-size: 23px; }
  .package--basic .package__title { height: 75px; font-size: 22px; line-height: 28px; }
  .package--perpetual .package__title { height: 78px; font-size: 22px; line-height: 28px; }

  .package__tagline {
    background: var(--paper);
    color: var(--maroon);
    font-style: italic; font-weight: 600; font-size: 15px; line-height: 22px;
    text-align: center;
    display: flex; align-items: center; justify-content: center;
    padding: 0 10px;
  }
  .package--seasonal .package__tagline { height: 68px; }
  .package--basic .package__tagline { height: 79px; }
  .package--perpetual .package__tagline { height: 69px; }

  .package__body {
    margin-top: 6px;
    flex: 1;
    background: var(--paper);
    border-radius: 0 0 22px 22px;
    display: flex; flex-direction: column; align-items: center;
    padding: 18px 16px 16px;
    text-align: center;
  }
  .feature-list { list-style: none; font-style: italic; font-size: 12.5px; line-height: 18px; }
  .feature-list li + li::before {
    content: ""; display: block;
    width: 34px; height: 2px; background: var(--orange);
    margin: 6px auto 8px;
  }
  .feature-list li.feature--plain::before { display: none; }
  .feature-list li.feature--plain { margin-top: 10px; }

  .term-prices { list-style: none; margin-top: auto; display: flex; flex-direction: column; gap: 7px; }
  .term-price {
    display: flex; width: 207px; height: 36px; border-radius: 18px; overflow: hidden;
    font-weight: 700; font-size: 20px; color: var(--paper);
  }
  .term-price__term { background: var(--charcoal); width: 58%; display: flex; align-items: center; justify-content: center; padding-left: 6px; }
  .term-price__cost { background: var(--maroon); flex: 1; display: flex; align-items: center; padding-left: 10px; }

  .monthly-price {
    margin-top: auto;
    width: 172px; height: 130px; border-radius: 22px; overflow: hidden;
    color: var(--paper); text-align: center;
  }
  .monthly-price__label { background: var(--charcoal); height: 66px; font-size: 19px; line-height: 24px; padding-top: 9px; }
  .monthly-price__amount { background: var(--maroon); height: 64px; font-weight: 700; font-size: 46px; line-height: 64px; }

  .package__note { font-size: 13px; line-height: 17px; margin-top: 20px; }
  .package__note--lock { margin-top: 40px; font-weight: 600; font-size: 12.5px; line-height: 16px; }
  .package__valid { font-size: 13px; margin-top: 8px; }
  .package--seasonal .package__valid { margin-top: 10px; }
</style>
</head>
<body>
<main class="flier">
  <header class="masthead">
    <span class="masthead__dot"></span>
    <span class="masthead__name">Hollowbrook Gardens</span>
  </header>

  <div class="hero-photo" role="img" aria-label="Photograph of granite headstones on a green lawn with trimmed boxwood shrubs"></div>
  <div class="footer-band"></div>

  <div class="year-badge">
    <div class="year-badge__year">2019</div>
    <div class="year-badge__title">LANDSCAPING<br>PACKAGES</div>
  </div>

  <section class="package package--seasonal">
    <h2 class="package__title">Seasonal Care</h2>
    <p class="package__tagline">Seasonal Landscaping<br>Grave Care</p>
    <div class="package__body">
      <ul class="feature-list">
        <li>Weeding and trimming services on your gravestite approximately every 7 weeks during the growing season: mid-April through mid-October</li>
      </ul>
      <ul class="term-prices">
        <li class="term-price"><span class="term-price__term">3 YEARS</span><span class="term-price__cost">$345</span></li>
        <li class="term-price"><span class="term-price__term">2 YEARS</span><span class="term-price__cost">$230</span></li>
        <li class="term-price"><span class="term-price__term">1 YEARS</span><span class="term-price__cost">$115</span></li>
      </ul>
      <p class="package__note package__note--lock">Multi-year payment locks<br>in current rates.</p>
      <p class="package__valid">Valid through 10.31.19.</p>
    </div>
  </section>

  <section class="package package--basic">
    <h2 class="package__title">Basic Care<br>Endownment</h2>
    <p class="package__tagline">Landscaping care forever<br>for graves with no plantings.</p>
    <div class="package__body">
      <ul class="feature-list">
        <li>Wedding and trimming service on your gravesite 2 times per years. mid-May and mid-September</li>
        <li>Monument leveling</li>
        <li class="feature--plain">Payment ensures grave care forever</li>
      </ul>
      <div class="monthly-price">
        <div class="monthly-price__label">12 MONTHLY<br>PAYMENT OF</div>
        <div class="monthly-price__amount">$239</div>
      </div>
      <p class="package__note">Call for single payment discount</p>
      <p class="package__valid">Valid through 10.31.19</p>
    </div>
  </section>

  <section class="package package--perpetual">
    <div class="package__flag">MOST POPULAR</div>
    <h2 class="package__title">Perpetual Care<br>Endownment</h2>
    <p class="package__tagline">Landscaping care forever<br>for graves with no plantings.</p>
    <div class="package__body">
      <ul class="feature-list">
        <li>Wedding and triming services on your gravesite approximately on your gravesite approximately every 7 weeks during the growing season: mid-April through mid-October.</li>
        <li>Monument leveling and cleaning</li>
        <li class="feature--plain">Payment ensures grave care forever</li>
        <li>Full bed of boxwood shrubs</li>
        <li>Replacement of shrubs</li>
        <li>Trust certificate</li>
      </ul>
      <div class="monthly-price">
        <div class="monthly-price__label">12 MONTHLY<br>PAYMENT OF</div>
        <div class="monthly-price__amount">$297</div>
      </div>
      <p class="package__note">Call for single payment discount</p>
      <p class="package__valid">Valid through 10.31.19</p>
    </div>
  </section>
</main>
</body>
</html>
```